Wall art for an Investments Lab at a college

Wall art for inside a new investments lab. A photo of the lab is attached. The wall art will go on the wall in the back right (pictured). It is currently white and the adjacent walls are white. The accent wall in the room is blue (summer nights). A copy of our color palette for environmental design is also attached. The tag line should be INVESTING IN THE FUTURE.

Target Market(s)

College students

Industry/Entity Type

Finance

Requirements
Must have
• Incorporate colors from palette

```html
<!DOCTYPE html>
<html lang="en">
<head>
<meta charset="utf-8">
<title>Investing in the Future</title>
<link rel="stylesheet" href="https://fonts.googleapis.com/css2?family=Oswald:wght@500;700&display=swap">
<style>
  :root {
    --wall-white: #ffffff;
    --summer-night: #03557a;
    --lagoon: #56c4c6;
    --mist: #eef3f6;
    --mist-soft: #f3f7f9;
  }
  html, body {
    margin: 0;
    padding: 0;
    width: 1200px;
    height: 1061px;
    overflow: hidden;
    background: var(--wall-white);
  }
  .wall-art {
    display: block;
    width: 1200px;
    height: 1061px;
  }
  .growth-bar { fill: var(--mist); }
  .growth-line {
    fill: none;
    stroke: var(--mist);
    stroke-width: 22;
    stroke-linejoin: miter;
  }
  .growth-arrowhead { fill: var(--mist); }
  .tagline {
    font-family: "Oswald", "Arial Narrow", sans-serif;
    font-weight: 700;
  }
  .tagline-lead { fill: var(--summer-night); }
  .tagline-small { fill: var(--lagoon); font-weight: 500; }
  .tagline-accent { fill: var(--lagoon); }
</style>
</head>
<body>
<svg class="wall-art" viewBox="0 0 1000 884" xmlns="http://www.w3.org/2000/svg">
  <defs>
    <radialGradient id="map-fade" cx="50%" cy="45%" r="60%">
      <stop offset="0%" stop-color="var(--mist-soft)"/>
      <stop offset="70%" stop-color="var(--mist-soft)"/>
      <stop offset="100%" stop-color="var(--wall-white)"/>
    </radialGradient>
  </defs>

  <rect class="world-map" x="40" y="70" width="960" height="500" rx="60"
        fill="url(#map-fade)" role="img" aria-label="Faint world map in the background"/>

  <g class="growth-chart">
    <rect class="growth-bar" x="52"  y="860" width="22" height="24"/>
    <rect class="growth-bar" x="80"  y="868" width="22" height="16"/>
    <rect class="growth-bar" x="108" y="828" width="22" height="56"/>
    <rect class="growth-bar" x="136" y="830" width="22" height="54"/>
    <rect class="growth-bar" x="164" y="838" width="22" height="46"/>
    <rect class="growth-bar" x="192" y="798" width="22" height="86"/>
    <rect class="growth-bar" x="220" y="800" width="22" height="84"/>
    <rect class="growth-bar" x="248" y="808" width="22" height="76"/>
    <rect class="growth-bar" x="276" y="768" width="22" height="116"/>
    <rect class="growth-bar" x="304" y="770" width="22" height="114"/>
    <rect class="growth-bar" x="332" y="778" width="22" height="106"/>
    <rect class="growth-bar" x="360" y="738" width="22" height="146"/>
    <rect class="growth-bar" x="388" y="740" width="22" height="144"/>
    <rect class="growth-bar" x="416" y="748" width="22" height="136"/>
    <rect class="growth-bar" x="444" y="708" width="22" height="176"/>
    <rect class="growth-bar" x="472" y="710" width="22" height="174"/>
    <rect class="growth-bar" x="500" y="718" width="22" height="166"/>
    <rect class="growth-bar" x="528" y="678" width="22" height="206"/>
    <rect class="growth-bar" x="556" y="680" width="22" height="204"/>
    <rect class="growth-bar" x="584" y="688" width="22" height="196"/>
    <rect class="growth-bar" x="612" y="648" width="22" height="236"/>
    <rect class="growth-bar" x="640" y="650" width="22" height="234"/>
    <rect class="growth-bar" x="668" y="658" width="22" height="226"/>
    <rect class="growth-bar" x="696" y="618" width="22" height="266"/>
    <rect class="growth-bar" x="724" y="620" width="22" height="264"/>
    <rect class="growth-bar" x="752" y="628" width="22" height="256"/>
    <rect class="growth-bar" x="780" y="588" width="22" height="296"/>
    <rect class="growth-bar" x="808" y="590" width="22" height="294"/>
    <rect class="growth-bar" x="836" y="598" width="22" height="286"/>
    <rect class="growth-bar" x="864" y="558" width="22" height="326"/>
    <rect class="growth-bar" x="892" y="560" width="22" height="324"/>
    <rect class="growth-bar" x="920" y="568" width="22" height="316"/>
    <rect class="growth-bar" x="948" y="528" width="22" height="356"/>
    <rect class="growth-bar" x="976" y="530" width="22" height="354"/>

    <polyline class="growth-line"
              points="10,800 180,715 240,745 470,610 520,640 870,390"/>
    <polygon class="growth-arrowhead" points="927,349 847,357 893,423"/>
  </g>

  <g class="tagline">
    <text class="tagline-lead" x="233" y="409" font-size="134"
          textLength="532" lengthAdjust="spacingAndGlyphs">INVESTING</text>
    <text class="tagline-small" x="233" y="531" font-size="84"
          textLength="187" lengthAdjust="spacingAndGlyphs">IN THE</text>
    <text class="tagline-accent" x="440" y="535" font-size="107"
          textLength="325" lengthAdjust="spacingAndGlyphs">FUTURE</text>
  </g>
</svg>
</body>
</html>
```